Emerging automotive detailing business

I am starting a small automotive detailing business in hopes of becoming a well-known detailer to work on high end cars. I would like a card to reflect the high quality and time I put into my work. The name of the company is Brightwater Kerb Detailing. I feel like it represents racecars getting off the line at the drag strip as well as an innuendo of "Up the Ladder". I do minor paint correction such as clay barring, multi-step buffing and polishing, waxing, hand washes, etc. I am always striving to learn more and improve my work. My goal is to have total customer satisfaction. This is a female run business but I do not want it to be very girly. Elegant is okay! I have pictures of my personal kestrel attached, they do not need to be incorporated but if you can think of a cool way to use 1 or all of them, go for it!

Target Market(s)

Anyone that owns a vehicle. Preferably high end vehicles such as Varello, Castenvaldi and Benotti but I will also happily work on any car, truck or suv no matter what brand.

Industry/Entity Type

Automotive

Contact Information for Business Card

Brightwater Kerb Detailing
Wendy Harlowe
4157 Quimby Hollow Rd
Red Lion PA 17492
Cell phone- call/text- 717-555-6284
email- brightwaterkerb@mailvale.test
Instagram: @brightwaterkerbdetail
Facebook: friendspage.test/brightwaterkerbdetail

Requirements
Must have
• Business name, my name, address, phone number. Listing that I do minor paint correction such as clay barring, multi-step buffing and polishing, waxing, hand washes, interior cleaning, and more. (This last part was in nice to haves but I have realized that I do really want it, so I moved it to must haves.) I want something that is different and eye-catching to my customers. Some people have done this very well with cards already submitted to me, but a lot have not. I didn't mess with the "look and feel bars" much because because I am pretty open to the overall design as long as it is not your basic run of the mill design.
Nice to have
• Something car related. Maybe an appointment time/date line. I do not have a logo, but if you would like to design one and incorporate it, that would be amazing!
Should not have
• Purple and Pink colors. Boring, basic, normal card.

```html
<!DOCTYPE html>
<html lang="en">
<head>
<meta charset="utf-8">
<title>Brightwater Kerb Detailing – Business Card</title>
<link href="https://fonts.googleapis.com/css2?family=Jost:wght@700&family=Lato:wght@400;700&display=swap" rel="stylesheet">
<style>
  :root {
    --page-bg: #ececec;
    --card-light: #f6f6f6;
    --card-dark: #000000;
    --ink: #111111;
    --ink-soft: #444444;
    --ink-reverse: #f2f2f2;
    --photo-top: #9aa095;
    --photo-bottom: #5e5648;
  }
  * { box-sizing: border-box; margin: 0; padding: 0; }
  html, body { width: 1200px; height: 1000px; overflow: hidden; }
  body {
    background: var(--page-bg);
    font-family: "Lato", sans-serif;
    color: var(--ink);
    position: relative;
  }
  .card {
    position: absolute;
    width: 500px;
    height: 296px;
    display: flex;
    overflow: hidden;
  }
  .card--back { left: 345px; top: 156px; }
  .card--front { left: 347px; top: 523px; width: 495px; height: 293px; }

  /* Back: services + appointment */
  .services {
    width: 337px;
    background: var(--card-dark);
    color: var(--ink-reverse);
    list-style: none;
    padding: 70px 0 0 25px;
  }
  .services li {
    display: flex;
    align-items: center;
    font-size: 15px;
    height: 31.5px;
  }
  .services svg { width: 17px; height: 12px; margin-right: 8px; flex: none; }
  .appointment {
    flex: 1;
    background: var(--card-light);
    padding: 110px 0 0 8px;
  }
  .appointment h3 { font-size: 17px; font-weight: 700; margin-bottom: 18px; line-height: 20px; }
  .appointment p { font-size: 16.5px; color: var(--ink-soft); margin-bottom: 14px; line-height: 20px; }

  /* Front: identity + contact */
  .identity {
    width: 334px;
    background: var(--card-light);
    padding: 42px 0 0 20px;
  }
  .business-name {
    font-family: "Jost", sans-serif;
    font-weight: 700;
    font-size: 22px;
    color: var(--ink);
    line-height: 1.1;
  }
  .address { font-size: 14.5px; color: var(--ink-soft); margin-top: 12px; }
  .person { font-size: 24px; font-weight: 400; margin-top: 56px; }
  .contact { list-style: none; margin-top: 8px; }
  .contact li { font-size: 14.5px; color: var(--ink-soft); line-height: 21px; }
  .contact strong { color: var(--ink); font-weight: 700; }
  .photo {
    flex: 1;
    background: linear-gradient(180deg, var(--photo-top) 0%, var(--photo-bottom) 100%);
  }
</style>
</head>
<body>
  <section class="card card--back">
    <ul class="services">
      <li><svg viewBox="0 0 17 12"><path d="M0 0 L17 6 L0 12 L4 6 Z" fill="currentColor"/></svg>Clay barring,</li>
      <li><svg viewBox="0 0 17 12"><path d="M0 0 L17 6 L0 12 L4 6 Z" fill="currentColor"/></svg>Multi-step buffing and polishing</li>
      <li><svg viewBox="0 0 17 12"><path d="M0 0 L17 6 L0 12 L4 6 Z" fill="currentColor"/></svg>Waxing</li>
      <li><svg viewBox="0 0 17 12"><path d="M0 0 L17 6 L0 12 L4 6 Z" fill="currentColor"/></svg>Hand washes</li>
      <li><svg viewBox="0 0 17 12"><path d="M0 0 L17 6 L0 12 L4 6 Z" fill="currentColor"/></svg>Interior cleaning and more.</li>
    </ul>
    <div class="appointment">
      <h3>Appointment</h3>
      <p>Date</p>
      <p>Time</p>
    </div>
  </section>

  <section class="card card--front">
    <div class="identity">
      <h1 class="business-name">Brightwater Kerb Detailing</h1>
      <p class="address">4157 Quimby Hollow Rd, Red Lion PA 17492</p>
      <h2 class="person">Wendy Harlowe</h2>
      <ul class="contact">
        <li><strong>Cell:</strong> 717-555-6284</li>
        <li><strong>Instagram:</strong> @brightwaterkerbdetail</li>
        <li><strong>Email-</strong> brightwaterkerb@mailvale.test</li>
      </ul>
    </div>
    <div class="photo" role="img" aria-label="Photo placeholder: owner's car parked outdoors"></div>
  </section>
</body>
</html>
```